Business Cards & Stationery for a Gold Refiner
Brambleton Assets
Business Cards & Stationery for a Gold Refiner - Jewelry
Creative Brief
Professional
(MUST BE LEFT BLANK)
18 East 52nd Street, Lobby Rear, New York, NY 10022
(212)-584-MINT (6468)
info@brambletonassetsllc.example
Hey Designers, We would like for our telephone, fax, and email to be titled with symbols instead of words, e.g. a small telephone symbol next to the phone number and a fax machine next to the fax number. We require blank fields we can fill in, with no symbols, for: NAME, TITLE We require blank fields we can fill in, with symbols, for: CELL NUMBER, EMAIL, WEB ADDRESS Also, and this point is VERY IMPORTANT, we need the final deliverables to include an editable Adobe Illustrator and/or Photoshop file (preferably, Illustrator). We will include the names and titles of our individual employees ourselves, thus we need those sections to be left blank. All fields should be editable. We will not accept the design if it does not include a fully editable file. Our logo was recently completed and we require it to be included in the design. The file should be attached to the contest. We have additional versions of the logo we'd like to be able to swap out at will, however they are all in the same style as the logo provided, so the color scheme of the logo should be utilized throughout. The font should be traditional and corporate in style, and not too stylized or flashy. The logo should be included on the back as well. Thanks Everybody and Good Luck!

```html
<!DOCTYPE html>
<html lang="en">
<head>
<meta charset="utf-8">
<title>Brambleton Assets — Business Cards</title>
<link rel="stylesheet" href="https://fonts.googleapis.com/css2?family=Questrial&display=swap">
<style>
  :root {
    --page-bg: #e9e7e3;
    --card-bg: #ffffff;
    --gold: #d6a41e;
    --slate: #5f6062;
    --ink: #3c3d3f;
    --shadow: rgba(0, 0, 0, 0.18);
  }
  * { margin: 0; padding: 0; box-sizing: border-box; }
  html, body {
    width: 1200px;
    height: 904px;
    overflow: hidden;
    background: var(--page-bg);
    font-family: "Questrial", "Century Gothic", sans-serif;
  }
  .canvas {
    position: relative;
    width: 1200px;
    height: 904px;
  }
  .card {
    position: absolute;
    width: 540px;
    height: 309px;
    background: var(--card-bg);
    border-radius: 18px;
    box-shadow: 0 6px 18px var(--shadow);
  }
  .card--front { left: 90px; top: 110px; }
  .card--back  { left: 570px; top: 485px; }

  .wordmark {
    position: absolute;
    display: flex;
    align-items: center;
    gap: 10px;
    left: 50%;
    transform: translateX(-50%);
    white-space: nowrap;
  }
  .wordmark__square {
    width: 26px;
    height: 26px;
    background: var(--gold);
  }
  .wordmark__name {
    font-size: 27px;
    letter-spacing: 0.5px;
    color: var(--slate);
    text-transform: uppercase;
  }
  .card--front .wordmark { top: 138px; }
  .card--back .wordmark { top: 118px; }

  .contact {
    position: absolute;
    left: 0;
    right: 0;
    text-align: center;
    color: var(--ink);
    font-size: 12.5px;
  }
  .contact--address { top: 190px; }
  .contact--lines {
    top: 214px;
    display: flex;
    justify-content: center;
    align-items: center;
    gap: 8px;
  }
  .contact__item {
    display: inline-flex;
    align-items: center;
    gap: 5px;
  }
  .contact__icon {
    width: 12px;
    height: 12px;
    fill: var(--gold);
  }
  .contact__divider { color: var(--ink); }
</style>
</head>
<body>
<main class="canvas">

  <section class="card card--front" aria-label="Business card front">
    <div class="wordmark">
      <span class="wordmark__square"></span>
      <span class="wordmark__name">Brambleton Assets</span>
    </div>
  </section>

  <section class="card card--back" aria-label="Business card back">
    <div class="wordmark">
      <span class="wordmark__square"></span>
      <span class="wordmark__name">Brambleton Assets</span>
    </div>

    <p class="contact contact--address">18 East 52nd Street, Lobby Rear, New York, NY 10022</p>

    <div class="contact contact--lines">
      <span class="contact__item">
        <svg class="contact__icon" viewBox="0 0 24 24" aria-hidden="true">
          <path d="M6.6 10.8a15.1 15.1 0 0 0 6.6 6.6l2.2-2.2a1 1 0 0 1 1-.25 11.4 11.4 0 0 0 3.6.57 1 1 0 0 1 1 1V20a1 1 0 0 1-1 1A17 17 0 0 1 3 4a1 1 0 0 1 1-1h3.5a1 1 0 0 1 1 1c0 1.25.2 2.45.57 3.6a1 1 0 0 1-.25 1z"/>
        </svg>
        (212)-584-MINT (6468)
      </span>
      <span class="contact__divider">|</span>
      <span class="contact__item">
        <svg class="contact__icon" viewBox="0 0 24 24" aria-hidden="true">
          <path d="M6.6 10.8a15.1 15.1 0 0 0 6.6 6.6l2.2-2.2a1 1 0 0 1 1-.25 11.4 11.4 0 0 0 3.6.57 1 1 0 0 1 1 1V20a1 1 0 0 1-1 1A17 17 0 0 1 3 4a1 1 0 0 1 1-1h3.5a1 1 0 0 1 1 1c0 1.25.2 2.45.57 3.6a1 1 0 0 1-.25 1z"/>
        </svg>
        (212)-584-7720
      </span>
      <span class="contact__divider">|</span>
      <span class="contact__item">
        <svg class="contact__icon" viewBox="0 0 24 24" aria-hidden="true">
          <path d="M2 5h20v14H2zm2 2v.4l8 5.3 8-5.3V7zm0 2.8V17h16V9.8l-8 5.3z"/>
        </svg>
        info@brambletonassetsllc.example
      </span>
    </div>
  </section>

</main>
</body>
</html>
```